Halt and Thicken New Branding Stationary Set - updated Oct 30th 2017

Updated on 30th Oct 2017 as we now need a whole folder design instead of a folder cover. We have thought out exactly what should be on it so it wont be hard. We are happy for this to be completed only by the winning designer if you like. And also we are guaranteeing this project now. Thanks!

We just got our new logo and now we would like a stationary set so we can brand our company communications. The items we need designed are:
Business cards
Letterhead
Appointment confirmation cards
Folder - switched from folder cover. Note that if you don't wish to do this unless you are selected as the winner this is fine.

1. Business cards - for 5 employees, final names will be given once the winner is selected, but you can use this one as the sample:
Lucinda Marquez
Hair Regrowth Expert
Halt and Thicken
7182 Oakmere Ave, Suite 500
Beverly Hills CA 90299
lucinda@jamesholloway-md.example
(310) 555-0193

2. Letterhead 8.5" x 11.0" vertical
Halt and Thicken
Beverly Hills CA 90299
office@haltandthicken.example
(310) 555-0193

3. Appointment Confirmation cards - business card size
Halt and Thicken
Beverly Hills CA 90299
Appointment For:
Date:
Time:
If you are unable to make your appointment, please contact us to reschedule at:
(310) 555-0193
info@jamesholloway-md.example

*UPDATED*
4. Folder 9" x 12 " vertical with double pocket
We would like the infinity image from the logo made really big so the left side is on the back and the right side with the + sign is on the front and its takes up the maximum room on the folder.
On the front below the half logo it should say "A Biochemical Revolution..."
On the inside we would also like to have the infinity sign from the logo but faded and half on the left pocket half on the right.
On left inside pocket it should say (this will be partically written on top of the logo):
James Holloway MD
Precision Medicine
Halt and Thicken Hair
On the Right inside pocket it should say the following:
Because the Enemy of BETTER Health is Good Health
BETTER Ingredients
BETTER Recipe
BETTER Medicine
On the back below the logo on the bottom should be the contact information.
I attached a picture of our drawing of what we want for this to make it easier.

Here is our website to give you an idea of our branding: http://www.haltandthicken.example/

We are the only true cure for hair loss and need to look professional and highest quality and beyond reproach from an ethical standpoint. We are a medical clinic so this should be portrayed also.
We cured hair loss by analyzing biochemistry and rebalancing it so that the process reverses and your own hair can grow back naturally.

Business card information:

OK so here is the information for the business cards:

Lucinda Marquez
Hair Regrowth Expert
(310) 555-0193
www.haltandthicken.example

Marisol Quintero
Hair Growth Consultant
(310) 555-0193
marisol@jamesholloway-md.example
www.haltandthicken.example

Janice Pelham
CMO/COO
(310) 555-0193
janice@haltandthicken.example
www.haltandthicken.example

Dr Glen Holloway
President
(310) 555-0193
info@jamesholloway-md.example
www.haltandthicken.example

Halt and Thicken
Customer Service
(310) 555-0193
info@jamesholloway-md.example
www.haltandthicken.example

Target Market(s)

Men aged 20-24 who care about their appearance, care about their hair and care about the world.

Industry/Entity Type

Medical And Science

Font styles to use
Sans Serif

Colors
00a990
ffffff
9d9d9d
333333

Requirements
Must have
• Must use the logo and our brand colors from the logo in all designs.
• The pantone colors are:
• Green: #4ca26f
• Light Grey: #999999
• The design should be symmetrical and balanced.
Nice to have
• It should look reasonably masculine.
Should not have
• Do not include any red in the design.

```html
<!DOCTYPE html>
<html lang="en">
<head>
<meta charset="utf-8">
<title>Halt and Thicken – Business Card</title>
<link href="https://fonts.googleapis.com/css2?family=Open+Sans:wght@400;600;700&display=swap" rel="stylesheet">
<style>
  :root {
    --brand-green: #4ca26f;
    --brand-grey: #999999;
    --ink: #4a4a4a;
    --card-dark: #333333;
    --card-light: #ffffff;
    --stage: #e6e7e8;
  }
  * { box-sizing: border-box; margin: 0; padding: 0; }
  html, body { width: 1200px; height: 904px; overflow: hidden; }
  body {
    background: var(--stage);
    font-family: "Open Sans", Arial, sans-serif;
    position: relative;
  }
  .card {
    position: absolute;
    left: 290px;
    width: 620px;
    height: 354px;
    border-radius: 22px;
    overflow: hidden;
    box-shadow: 0 6px 18px rgba(0,0,0,.18);
  }
  .card--back { top: 60px; background: var(--card-dark); }
  .card--front { top: 480px; background: var(--card-light); }

  .wordmark {
    position: absolute;
    left: 0; right: 0;
    display: flex;
    align-items: center;
    justify-content: center;
    gap: 16px;
    font-weight: 700;
    color: var(--brand-green);
    letter-spacing: .5px;
  }
  .wordmark__dot {
    border-radius: 50%;
    background: var(--brand-green);
  }
  .card--back .wordmark { top: 150px; font-size: 40px; }
  .card--back .wordmark__dot { width: 34px; height: 34px; }
  .card--front .wordmark { top: 40px; font-size: 28px; }
  .card--front .wordmark__dot { width: 24px; height: 24px; }

  .person {
    position: absolute;
    top: 104px; left: 0; right: 0;
    text-align: center;
  }
  .person__name { color: var(--brand-green); font-weight: 700; font-size: 20px; }
  .person__title { color: var(--ink); font-size: 15px; margin-top: 2px; }

  .details {
    position: absolute;
    top: 190px; left: 0; right: 0;
    display: flex;
    justify-content: center;
  }
  .address {
    text-align: right;
    color: var(--ink);
    font-size: 15px;
    line-height: 1.4;
    padding-right: 18px;
  }
  .address__company { font-weight: 700; }
  .divider { width: 1.5px; background: var(--ink); }
  .contact {
    list-style: none;
    padding-left: 14px;
    color: var(--ink);
    font-size: 15px;
    line-height: 1.4;
  }
  .contact li { display: flex; align-items: center; gap: 8px; }
  .contact svg { width: 13px; height: 13px; flex: none; }

  .edge-band {
    position: absolute;
    bottom: 0; left: 0; right: 0;
    height: 12px;
    display: flex;
  }
  .edge-band__grey { width: 52%; background: var(--brand-grey); }
  .edge-band__green { flex: 1; background: var(--brand-green); }
</style>
</head>
<body>
  <section class="card card--back" aria-label="Business card back">
    <div class="wordmark"><span class="wordmark__dot"></span>Halt and Thicken</div>
  </section>

  <section class="card card--front" aria-label="Business card front">
    <div class="wordmark"><span class="wordmark__dot"></span>Halt and Thicken</div>

    <div class="person">
      <p class="person__name">Lucinda Marquez</p>
      <p class="person__title">Hair Regrowth Expert</p>
    </div>

    <div class="details">
      <address class="address" style="font-style:normal">
        <div class="address__company">Halt and Thicken</div>
        <div>7182 Oakmere Ave, Suite 500</div>
        <div>Beverly Hills CA 90299</div>
      </address>
      <div class="divider"></div>
      <ul class="contact">
        <li>
          <svg viewBox="0 0 16 16" aria-hidden="true"><path fill="#4ca26f" d="M3 1l3 3-1.5 2c1 2 3.5 4.5 5.5 5.5L12 10l3 3-2 2C7 15 1 9 1 3z"/></svg>
          (310) 555-0193
        </li>
        <li>
          <svg viewBox="0 0 16 16" aria-hidden="true"><rect x="1" y="3" width="14" height="10" rx="1" fill="#4ca26f"/><path d="M1.5 3.5L8 9l6.5-5.5" stroke="#fff" stroke-width="1.4" fill="none"/></svg>
          lucinda@jamesholloway-md.example
        </li>
        <li>
          <svg viewBox="0 0 16 16" aria-hidden="true"><circle cx="8" cy="8" r="7" fill="#4ca26f"/><path d="M1 8h14M8 1c-3 3-3 11 0 14M8 1c3 3 3 11 0 14" stroke="#fff" stroke-width="1" fill="none"/></svg>
          www.jamesholloway-md.example
        </li>
      </ul>
    </div>

    <div class="edge-band">
      <span class="edge-band__grey"></span>
      <span class="edge-band__green"></span>
    </div>
  </section>
</body>
</html>
```